Mobile app for checking bus arrival

I would like to make the UI much more beautiful and modern. The app is an app to check bus arrival in Singapore.
See here: https://apps.veltrixa.com/store/apps/details?id=com.ridetrk&hl=en

Based on the question from designers:

1. The first screen shows the favorite bus stop. Each item shows location / street, the top one is the location, second line is the street name. And the number is the bus stop code.

2. Please download the app and try bus stop code with 07589 or 10079, for example. It will bring you to the next screen.

3. The pencil allow you to select color theme, for the list item, and the header.

4. On the second screen, it will show up the list of bus route that available on that bus stop.

5. When you tap on one of them it will show you the 2 subsequent arrival time.

6. Each of the arrival time has the information of availability seats available, seats not available, no more space. (we can use green, yellow, red, respectively).

7. Each of the arrival time has the WAB indicator (Wheelchair availability). Show as icon is preferred.

7. KLV and DPWQ are the bus provider in Singapore. 48 means the route /service no.

Requirements:
And check the attachment, see screen 3. I need to add information about the space availability, which has 3 state: seats available, seats not available, no more space. (we can use green, yellow, red, respectively).

Please advise how to show the information.

Target Market(s)

Students, age below 35

Industry/Entity Type

Veltrixa

Requirements
Must have
• The app currently has the capabilities to select color theme, checkout screen1. It's the button and the list item color.
Nice to have
• Please download the app to see all available colors, and make suggestion to have better color pallete.

```html
<!DOCTYPE html>
<html lang="en">
<head>
<meta charset="utf-8">
<title>Bus Arrival – Stop 07589</title>
<link rel="stylesheet" href="https://fonts.googleapis.com/css2?family=Roboto:wght@400;500&display=swap">
<style>
  :root {
    --page-bg: #e4e4e4;
    --status-bar: #4b2a82;
    --app-bar: #6a3db8;
    --brand-text: #6a3db8;
    --list-bg: #eef1f5;
    --card-bg: #ffffff;
    --route-bg: #f3f5f8;
    --divider: #e4e7ec;
    --muted: #555b63;
    --ink: #2f3237;
    --star: #f5b22b;
    --op-klv: #e8363c;
    --op-dpwq: #5263dd;
    --seats: #3cb834;
    --standing: #f5a013;
    --full: #f25454;
    --wab-on: #33363b;
    --wab-off: #dfe2e6;
  }
  * { box-sizing: border-box; margin: 0; padding: 0; }
  html, body {
    width: 960px; height: 1200px; overflow: hidden;
    background: var(--page-bg);
    font-family: "Roboto", sans-serif;
  }
  .screen {
    position: absolute; left: 147px; top: 9px;
    width: 564px; height: 1002px;
    transform: scale(1.18); transform-origin: top left;
    background: var(--list-bg);
    overflow: hidden;
  }
  .status-bar {
    height: 38px; background: var(--status-bar);
    display: flex; align-items: center; justify-content: flex-end;
    gap: 10px; padding-right: 14px; color: #fff; font-size: 20px;
  }
  .app-bar {
    height: 87px; background: var(--app-bar); color: #fff;
    position: relative;
  }
  .app-bar .back { position: absolute; left: 34px; top: 31px; }
  .app-bar .title { position: absolute; left: 77px; top: 24px; font-size: 31px; letter-spacing: .5px; }
  .app-bar .refresh { position: absolute; left: 454px; top: 28px; }
  .app-bar .menu { position: absolute; left: 520px; top: 30px; }
  .stop-header {
    height: 127px; background: var(--card-bg); position: relative;
    border-bottom: 3px solid #e5dcf3;
    box-shadow: 0 2px 4px rgba(0,0,0,.06);
  }
  .stop-name { position: absolute; left: 28px; top: 27px; font-size: 30px; font-weight: 500; color: var(--brand-text); }
  .stop-road { position: absolute; left: 28px; top: 78px; font-size: 18px; color: var(--brand-text); }
  .stop-header .favourite { position: absolute; left: 488px; top: 40px; }
  .columns { position: relative; height: 63px; font-size: 17px; color: var(--muted); }
  .columns span { position: absolute; top: 30px; transform: translateX(-50%); }
  .route-list { position: relative; }
  .row {
    position: absolute; left: 15px; width: 533px; height: 105px;
    background: var(--card-bg); border-radius: 2px;
    box-shadow: 0 1px 2px rgba(0,0,0,.08);
  }
  .route {
    position: absolute; left: 0; top: 0; width: 121px; height: 105px;
    background: var(--route-bg); text-align: center;
  }
  .route .operator { display: block; margin-top: 24px; font-size: 17px; }
  .route .number { display: block; margin-top: 2px; font-size: 32px; color: var(--ink); }
  .op-klv { color: var(--op-klv); }
  .op-dpwq { color: var(--op-dpwq); }
  .chevron { position: absolute; left: 314px; top: 0; }
  .arrival { position: absolute; top: 0; height: 105px; width: 140px; }
  .arrival.next { left: 151px; }
  .arrival.subsequent { left: 356px; }
  .count { position: absolute; left: 0; width: 110px; top: 26px; text-align: center; line-height: 1; }
  .count .value { display: block; font-size: 34px; }
  .count .unit { display: block; font-size: 16px; margin-top: 0; }
  .count.full .value { font-size: 24px; margin-top: 6px; }
  .count.full .unit { margin-top: 1px; }
  .seats { color: var(--seats); }
  .standing { color: var(--standing); }
  .full { color: var(--full); }
  .wab { position: absolute; left: 108px; top: 38px; }
  .wab.on { color: var(--wab-on); }
  .wab.off { color: var(--wab-off); }
</style>
</head>
<body>
<svg width="0" height="0" style="position:absolute">
  <symbol id="wheelchair" viewBox="0 0 24 26">
    <circle cx="11" cy="3" r="2.4" fill="currentColor"/>
    <path d="M9.6 7h2.8v5.5h5.2l2.6 7.3 2-.7.7 2-4.1 1.4-2.6-7.2H9.6z" fill="currentColor"/>
    <path d="M7.8 11.2A6.4 6.4 0 1 0 16.2 19" fill="none" stroke="currentColor" stroke-width="2.4"/>
  </symbol>
</svg>

<main class="screen">
  <div class="status-bar">
    <svg width="20" height="18" viewBox="0 0 20 18"><path d="M18 1v16H2z" fill="#fff" opacity=".45"/><path d="M12 7v10H2z" fill="#fff"/></svg>
    <svg width="14" height="22" viewBox="0 0 14 22"><rect x="4" y="0" width="6" height="3" fill="#fff" opacity=".5"/><rect x="1" y="2" width="12" height="20" rx="1" fill="#fff" opacity=".5"/><rect x="1" y="11" width="12" height="11" fill="#fff"/></svg>
    <span class="clock">12:30</span>
  </div>

  <header class="app-bar">
    <svg class="back" width="22" height="24" viewBox="0 0 22 24"><path d="M14 3 5 12l9 9" fill="none" stroke="#fff" stroke-width="2.6" stroke-linecap="round" stroke-linejoin="round"/></svg>
    <span class="title">07589</span>
    <svg class="refresh" width="32" height="32" viewBox="0 0 32 32"><path d="M25 16a9 9 0 1 1-3-6.7" fill="none" stroke="#fff" stroke-width="3" stroke-linecap="round"/><path d="M25 4v8h-8z" fill="#fff"/></svg>
    <svg class="menu" width="10" height="28" viewBox="0 0 10 28"><circle cx="5" cy="4" r="3" fill="#fff"/><circle cx="5" cy="14" r="3" fill="#fff"/><circle cx="5" cy="24" r="3" fill="#fff"/></svg>
  </header>

  <section class="stop-header">
    <h1 class="stop-name">Opp Meranti Ctr</h1>
    <p class="stop-road">Kestrel Rd</p>
    <svg class="favourite" width="48" height="48" viewBox="0 0 24 24"><path d="M12 2.2l2.9 6.4 7 .7-5.3 4.7 1.5 6.9L12 17.4l-6.1 3.5 1.5-6.9L2.1 9.3l7-.7z" fill="var(--star)"/></svg>
  </section>

  <div class="columns">
    <span style="left:74px">Bus No.</span>
    <span style="left:240px">Next</span>
    <span style="left:445px">Subsequent</span>
  </div>

  <section class="route-list">
    <!-- row template repeated -->
    <article class="row" style="top:1px">
      <div class="route"><span class="operator op-klv">KLV</span><span class="number">48</span></div>
      <div class="arrival next"><div class="count seats"><span class="value">7</span><span class="unit">seats</span></div><svg class="wab on" width="24" height="26"><use href="#wheelchair"/></svg></div>
      <svg class="chevron" width="20" height="105"><path d="M1 0l17 52L1 105" fill="none" stroke="var(--divider)" stroke-width="1.2"/></svg>
      <div class="arrival subsequent"><div class="count seats"><span class="value">21</span><span class="unit">seats</span></div><svg class="wab on" width="24" height="26"><use href="#wheelchair"/></svg></div>
    </article>

    <article class="row" style="top:118px">
      <div class="route"><span class="operator op-klv">KLV</span><span class="number">57</span></div>
      <div class="arrival next"><div class="count standing"><span class="value">0</span><span class="unit">seats</span></div><svg class="wab on" width="24" height="26"><use href="#wheelchair"/></svg></div>
      <svg class="chevron" width="20" height="105"><path d="M1 0l17 52L1 105" fill="none" stroke="var(--divider)" stroke-width="1.2"/></svg>
      <div class="arrival subsequent"><div class="count seats"><span class="value">12</span><span class="unit">seats</span></div><svg class="wab off" width="24" height="26"><use href="#wheelchair"/></svg></div>
    </article>

    <article class="row" style="top:235px">
      <div class="route"><span class="operator op-klv">KLV</span><span class="number">130</span></div>
      <div class="arrival next"><div class="count full"><span class="value">No</span><span class="unit">Space</span></div><svg class="wab on" width="24" height="26"><use href="#wheelchair"/></svg></div>
      <svg class="chevron" width="20" height="105"><path d="M1 0l17 52L1 105" fill="none" stroke="var(--divider)" stroke-width="1.2"/></svg>
      <div class="arrival subsequent"><div class="count seats"><span class="value">8</span><span class="unit">seats</span></div><svg class="wab on" width="24" height="26"><use href="#wheelchair"/></svg></div>
    </article>

    <article class="row" style="top:352px">
      <div class="route"><span class="operator op-dpwq">DPWQ</span><span class="number">851</span></div>
      <div class="arrival next"><div class="count standing"><span class="value">0</span><span class="unit">seats</span></div><svg class="wab off" width="24" height="26"><use href="#wheelchair"/></svg></div>
      <svg class="chevron" width="20" height="105"><path d="M1 0l17 52L1 105" fill="none" stroke="var(--divider)" stroke-width="1.2"/></svg>
      <div class="arrival subsequent"><div class="count seats"><span class="value">16</span><span class="unit">seats</span></div><svg class="wab on" width="24" height="26"><use href="#wheelchair"/></svg></div>
    </article>

    <article class="row" style="top:469px">
      <div class="route"><span class="operator op-dpwq">DPWQ</span><span class="number">960</span></div>
      <div class="arrival next"><div class="count seats"><span class="value">7</span><span class="unit">seats</span></div><svg class="wab on" width="24" height="26"><use href="#wheelchair"/></svg></div>
      <svg class="chevron" width="20" height="105"><path d="M1 0l17 52L1 105" fill="none" stroke="var(--divider)" stroke-width="1.2"/></svg>
      <div class="arrival subsequent"><div class="count seats"><span class="value">8</span><span class="unit">seats</span></div><svg class="wab on" width="24" height="26"><use href="#wheelchair"/></svg></div>
    </article>

    <article class="row" style="top:586px">
      <div class="route"><span class="operator op-klv">KLV</span><span class="number">2N</span></div>
      <div class="arrival next"><div class="count seats"><span class="value">12</span><span class="unit">seats</span></div><svg class="wab off" width="24" height="26"><use href="#wheelchair"/></svg></div>
      <svg class="chevron" width="20" height="105"><path d="M1 0l17 52L1 105" fill="none" stroke="var(--divider)" stroke-width="1.2"/></svg>
      <div class="arrival subsequent"><div class="count seats"><span class="value">19</span><span class="unit">seats</span></div><svg class="wab on" width="24" height="26"><use href="#wheelchair"/></svg></div>
    </article>
  </section>
</main>
</body>
</html>
```